Healthy Snack/Confectionery Bar Logo & front of pack

KOVA LUMEN LOGO and ON PACK
Directionally, use of colours specified in the brief is important as consumers associate the brand values we want with these colours. Blue. Green Cyan on White background should probably be the base colours. Gradients and Swirls of Colour would be good, but welcome alternatives. Product imagery should be in a set window that works well with the logo design.

Core Target Audience: Adults seeking to reduce/avoid sugar due to health concerns (pre-diabetic/diabetic/sugar avoiders), Secondary Audiences: Healthcare professionals looking for strategies to reduce sugar consumption, Mothers seeking to reduce family sugar consumption. Core Design Objectives: “HEALTHY AND PREMIUM” “FRESH” / Tasty / Appetising (product illustration) / Premium, Natural and Low in Sugar (colour cues) / Expert / Effective / Recommended (endorsements and back of pack).
Cyan/Blue often used to denote No added Sugar. Cyan = R 0 G 255 B 255
Blue/Green often used to denote medical benefit. Blue= R 0 G 129 B 129 / Green= R 132 G 173 B 0
Kova Lumen Yellow – R 254 G 244 B 0 links to QRB Brand.
* RGB Values for Cyan and Blue and Green are for Guidance only.

Text & Fonts: No more than 6 words. Largest - KOVA LUMEN (KOVA to be subservient / more in the background - LUMEN should stand out as the main word. Medium - PELLOW DRIFT - Medium & integrated into design - LOW KOVA
Fonts Decorative – e.g. MICROBREW, PHOPSPHATE, CAMPUS, INTRO RUST, BURFORD RUSTIC (see glyphhaven.net)

Target Market(s)

UK / NORTHERN EUROPE / AFLLUENT

Font styles to use
Sans Serif
Decorative

Colors
ffffff
0455a3
add136
fbee3d
000000
34a7d8

Requirements
Must have
• The design is for a healthy snack bar logo. Ideally the files submitted should include the image in an on-pack situation (e.g. a cereal bar, flapjack or cookie)
Nice to have
• See brief.

```html
<!DOCTYPE html>
<html lang="en">
<head>
<meta charset="utf-8">
<title>Kova Lumen – Pellow Drift front of pack</title>
<link rel="stylesheet" href="https://fonts.googleapis.com/css2?family=Teko:wght@600;700&family=Righteous&display=swap">
<style>
  :root {
    --backdrop: #eeeeec;
    --seal-blue: #27a3cf;
    --seal-blue-deep: #1582ad;
    --seal-green: #a9d12f;
    --seal-green-deep: #86ad14;
    --cocoa: #4a1d16;
    --cocoa-deep: #2e0f0b;
    --cocoa-light: #6b3026;
    --lumen-yellow: #e8ec3c;
    --leaf-green: #add136;
    --label-blue: #34a7d8;
    --crumb-light: #d9a766;
    --crumb-dark: #8a5226;
  }
  * { box-sizing: border-box; margin: 0; padding: 0; }
  html, body { width: 1200px; height: 900px; overflow: hidden; }
  body { background: var(--backdrop); position: relative; font-family: "Teko", sans-serif; }

  .pack { position: absolute; left: 335px; top: 50px; width: 530px; height: 800px; }

  .seal { position: absolute; left: 0; width: 100%; }
  .seal--top {
    top: 0; height: 140px;
    background:
      repeating-linear-gradient(180deg, rgba(255,255,255,0) 0 7px, rgba(0,0,0,.08) 7px 9px) top / 100% 75px no-repeat,
      linear-gradient(180deg, var(--seal-blue) 0%, var(--seal-blue-deep) 55%, var(--seal-blue) 100%);
    border-radius: 0 0 50% 50% / 0 0 14px 14px;
    z-index: 2;
  }
  .seal--bottom {
    bottom: 0; height: 140px;
    background:
      repeating-linear-gradient(180deg, rgba(255,255,255,0) 0 7px, rgba(0,0,0,.1) 7px 9px) bottom / 100% 85px no-repeat,
      linear-gradient(180deg, var(--seal-green) 0%, var(--seal-green-deep) 50%, var(--seal-green) 100%);
    z-index: 2;
  }
  .crimp { position: absolute; left: 0; width: 100%; height: 14px; z-index: 3; }
  .crimp--top { top: 0; }
  .crimp--bottom { bottom: 0; transform: scaleY(-1); }

  .product-window {
    position: absolute; left: 14px; right: 14px; top: 105px; height: 212px;
    background:
      radial-gradient(circle at 22% 45%, var(--crumb-dark) 0 26px, transparent 28px),
      radial-gradient(circle at 74% 82%, var(--crumb-dark) 0 28px, transparent 30px),
      linear-gradient(135deg, var(--crumb-light), #b97b3f 50%, var(--crumb-light));
    z-index: 1;
  }

  .low-sugar {
    position: absolute; left: 187px; top: 123px; width: 143px; height: 102px;
    background: var(--label-blue);
    display: flex; flex-direction: column; align-items: center; justify-content: center;
    color: var(--cocoa); line-height: .85; z-index: 4;
  }
  .low-sugar__big { font-size: 50px; font-weight: 700; }
  .low-sugar__small { font-size: 36px; font-weight: 600; }

  .cocoa-panel {
    position: absolute; left: 0; right: 0; top: 315px; height: 350px;
    background:
      linear-gradient(155deg, transparent 20%, rgba(255,255,255,.08) 30%, transparent 40%, rgba(0,0,0,.25) 55%, transparent 68%, rgba(255,255,255,.06) 80%, transparent 90%),
      linear-gradient(180deg, var(--cocoa-light), var(--cocoa) 30%, var(--cocoa-deep) 100%);
    z-index: 1;
  }

  .new-burst { position: absolute; left: 52px; top: 285px; width: 120px; height: 105px; z-index: 4; }

  .brand-band {
    position: absolute; left: 127px; top: 420px; width: 315px; height: 63px;
    background: var(--lumen-yellow);
    display: flex; align-items: center; justify-content: center;
    font-size: 62px; font-weight: 700; letter-spacing: 28px; padding-left: 28px;
    color: var(--cocoa); line-height: 1; padding-top: 10px; z-index: 4;
  }
  .brand-name {
    position: absolute; left: 95px; top: 478px; width: 330px; text-align: center;
    font-size: 150px; font-weight: 700; line-height: 1; letter-spacing: 2px;
    color: var(--lumen-yellow); z-index: 4;
  }
  .flavour {
    position: absolute; left: 80px; top: 605px; width: 350px; text-align: center;
    font-family: "Righteous", sans-serif; font-size: 34px; letter-spacing: 2px;
    color: var(--leaf-green); z-index: 4;
  }
</style>
</head>
<body>
  <main class="pack" aria-label="Kova Lumen Pellow Drift snack bar front of pack">
    <div class="seal seal--top"></div>
    <svg class="crimp crimp--top" viewBox="0 0 530 14" preserveAspectRatio="none" aria-hidden="true">
      <path fill="#eeeeec" d="M0 0H530V14L520 4 510 14 500 4 490 14 480 4 470 14 460 4 450 14 440 4 430 14 420 4 410 14 400 4 390 14 380 4 370 14 360 4 350 14 340 4 330 14 320 4 310 14 300 4 290 14 280 4 270 14 260 4 250 14 240 4 230 14 220 4 210 14 200 4 190 14 180 4 170 14 160 4 150 14 140 4 130 14 120 4 110 14 100 4 90 14 80 4 70 14 60 4 50 14 40 4 30 14 20 4 10 14 0 4Z"/>
    </svg>

    <div class="product-window" role="img" aria-label="Close-up photo of a crunchy oat bar with cocoa pieces"></div>

    <div class="low-sugar">
      <span class="low-sugar__big">LOW</span>
      <span class="low-sugar__small">SUGAR</span>
    </div>

    <div class="cocoa-panel"></div>

    <svg class="new-burst" viewBox="0 0 120 105" aria-label="New">
      <polygon fill="#add136" points="60,0 70,24 92,8 86,34 116,30 94,50 120,66 90,70 100,98 74,82 62,105 52,82 26,100 32,72 2,72 26,52 4,32 34,34 26,8 48,24"/>
      <text x="60" y="66" text-anchor="middle" font-family="Teko, sans-serif" font-weight="700" font-size="36" fill="#4a1d16">NEW</text>
    </svg>

    <div class="brand-band">KOVA</div>
    <h1 class="brand-name">LUMEN</h1>
    <p class="flavour">PELLOW DRIFT</p>

    <div class="seal seal--bottom"></div>
    <svg class="crimp crimp--bottom" viewBox="0 0 530 14" preserveAspectRatio="none" aria-hidden="true">
      <path fill="#eeeeec" d="M0 0H530V14L520 4 510 14 500 4 490 14 480 4 470 14 460 4 450 14 440 4 430 14 420 4 410 14 400 4 390 14 380 4 370 14 360 4 350 14 340 4 330 14 320 4 310 14 300 4 290 14 280 4 270 14 260 4 250 14 240 4 230 14 220 4 210 14 200 4 190 14 180 4 170 14 160 4 150 14 140 4 130 14 120 4 110 14 100 4 90 14 80 4 70 14 60 4 50 14 40 4 30 14 20 4 10 14 0 4Z"/>
    </svg>
  </main>
</body>
</html>
```